Notepads for Marketing pieces-BOLD design

Looking for notepads for marketing pieces with logo, phone number, and website. Maybe something faded in background. Looking for bold and different

```html
<!DOCTYPE html>
<html lang="en">
<head>
<meta charset="utf-8">
<title>Northvale Notepad</title>
<link rel="stylesheet" href="https://fonts.googleapis.com/css2?family=Montserrat:wght@500;600;800&display=swap">
<style>
  :root {
    --brand-red: #ff0000;
    --ink: #111111;
    --paper: #ffffff;
    --bar: #000000;
    --divider: #3a3a3a;
  }
  * { margin: 0; padding: 0; box-sizing: border-box; }
  html, body { width: 848px; height: 1200px; overflow: hidden; background: var(--paper); }
  body { font-family: "Montserrat", Arial, sans-serif; color: var(--ink); }

  .notepad { position: relative; width: 848px; height: 1200px; background: var(--paper); }

  .brand {
    position: absolute; left: 0; top: 0; width: 405px; height: 154px;
    display: flex; flex-direction: column; align-items: center; justify-content: center;
  }
  .brand-name {
    font-weight: 800; font-size: 44px; letter-spacing: 1px; color: var(--brand-red);
    line-height: 1; margin-top: 8px;
  }
  .brand-services {
    font-weight: 600; font-size: 10.5px; margin-top: 20px; white-space: nowrap;
  }

  .contact-panel {
    position: absolute; left: 405px; top: 0; width: 443px; height: 154px;
    background: var(--brand-red); color: var(--paper);
    padding: 34px 60px 0 0; text-align: right;
    font-size: 14.5px; font-weight: 500; line-height: 21.5px;
  }
  .contact-panel .company { font-weight: 600; }

  .website {
    position: absolute; left: 0; right: 0; top: 1106px;
    text-align: center; font-size: 20px; font-weight: 500; letter-spacing: 0.3px;
  }

  .social-bar {
    position: absolute; left: 0; bottom: 0; width: 848px; height: 46px;
    background: var(--bar); color: var(--paper); display: flex;
  }
  .social-item {
    flex: 1; display: flex; align-items: center; justify-content: center; gap: 12px;
    font-size: 14px; font-weight: 500;
  }
  .social-item + .social-item { border-left: 1px solid var(--divider); }
  .social-mark { width: 15px; height: 15px; background: var(--paper); border-radius: 2px; }
</style>
</head>
<body>
<main class="notepad">
  <header>
    <div class="brand">
      <div class="brand-name">NORTHVALE</div>
      <div class="brand-services">Home Health | Medical Staffing | Outpatient Therapy</div>
    </div>
    <address class="contact-panel" style="font-style:normal">
      <div class="company">Northvale Therapy Partners</div>
      <div>office@northvalecare.org</div>
      <div>555.201.0148 555.201.0392</div>
      <div>480 Meridian Parkway Lakeview, OH 43990</div>
    </address>
  </header>

  <footer>
    <div class="website">www.northvalecare.org</div>
    <div class="social-bar">
      <div class="social-item"><span class="social-mark"></span><span>northvalecare</span></div>
      <div class="social-item"><span class="social-mark"></span><span>@northvalecarellc</span></div>
      <div class="social-item"><span class="social-mark"></span><span>northvalecare</span></div>
    </div>
  </footer>
</main>
</body>
</html>
```